Lime Wash Direct Mail Postcard Design

I need a postcard that is going to be mailed.
We are a residential and commerical painting company. We are going to start marking our Ventian Plaster, Lime Wash, Roman Clay, Mineral Wash.
I've attached the layout to use that shows bleed and such. I've included a mock up I've done to get an idea of what I want.
- I want it to look sophicated
- Speciality
- Art
I've included logos of 2 companies - Kestiva and Dunmere to show.
I want to show mostly interior work but one or 2 lime wash houses that's lighter, shows the bricks in area would be good.
I love the saying "You're unique - Your Home Should Be Too" or if you have a better variation of that, I'd be open to it.

```html
<!DOCTYPE html>
<html lang="en">
<head>
<meta charset="utf-8">
<title>You're Unique – Specialty Finishes Postcard</title>
<link rel="stylesheet" href="https://fonts.googleapis.com/css2?family=Great+Vibes&family=Playfair+Display:wght@700;900&family=Questrial&display=swap">
<style>
  :root {
    --paper: #e9e9ea;
    --paper-deep: #cfcfd1;
    --panel: rgba(255, 255, 255, 0.82);
    --ink: #1d1d1f;
    --script-ink: #3b3b3d;
    --brand-ink: #333335;
    --navy: #152a6e;
    --royal: #1f4fa8;
    --sky: #2f7fd0;
    --link-blue: #2c6cc4;
    --rule: #5a5a5c;
  }
  * { margin: 0; padding: 0; box-sizing: border-box; }
  html, body { width: 1200px; height: 838px; overflow: hidden; }
  body { position: relative; background: var(--paper); font-family: "Questrial", sans-serif; }

  .backdrop {
    position: absolute; inset: 0;
    background:
      radial-gradient(ellipse at 20% 80%, #c9c9cb 0%, transparent 45%),
      radial-gradient(ellipse at 85% 75%, #d2d2d4 0%, transparent 40%),
      linear-gradient(160deg, #f1f1f2 0%, var(--paper) 50%, var(--paper-deep) 100%);
  }
  .panel {
    position: absolute; left: 57px; top: 46px; width: 1086px; height: 591px;
    background: var(--panel); border-radius: 22px;
  }
  .headline-word {
    position: absolute; left: 0; width: 1200px; text-align: center; line-height: 1;
  }
  .headline-unique {
    top: 222px; left: 12px;
    padding-bottom: 70px;
    font-family: "Playfair Display", serif; font-weight: 900; font-size: 204px;
    letter-spacing: -2px;
    background: linear-gradient(100deg, var(--navy) 0%, var(--royal) 30%, var(--sky) 48%, var(--royal) 66%, var(--navy) 100%);
    -webkit-background-clip: text; background-clip: text; color: transparent;
  }
  .headline-script {
    top: 105px; left: 10px;
    font-family: "Great Vibes", cursive; font-size: 186px; color: var(--script-ink);
  }
  .tagline {
    position: absolute; top: 442px; left: 0; width: 1200px; text-align: center;
    font-size: 63px; letter-spacing: 1px; color: var(--ink); line-height: 1.2;
  }
  .divider {
    position: absolute; left: 94px; top: 534px; width: 1011px; height: 2px; background: var(--rule);
  }
  .finish-list {
    position: absolute; top: 550px; left: 0; width: 1200px; list-style: none;
  }
  .finish-list li {
    position: absolute; top: 0;
    font-family: "Playfair Display", serif; font-weight: 700; font-size: 39px; line-height: 1.1;
    color: var(--link-blue); border-bottom: 2px solid var(--link-blue); padding-bottom: 2px; white-space: nowrap;
  }
  .finish-plaster { left: 98px; }
  .finish-lime { left: 397px; }
  .finish-clay { left: 613px; }
  .finish-mineral { left: 850px; }

  .project-photos { position: absolute; left: 0; top: 0; width: 1200px; height: 838px; }

  .brand-lockup {
    position: absolute; top: 696px; left: 660px; width: 488px; display: flex; align-items: center; justify-content: space-between;
    font-family: "Questrial", sans-serif; font-weight: 400; color: var(--brand-ink);
  }
  .brand-primary { font-size: 40px; letter-spacing: 5px; line-height: 1; }
  .brand-dot { width: 6px; height: 6px; border-radius: 50%; background: var(--brand-ink); }
  .brand-partner { font-size: 40px; letter-spacing: 3px; line-height: 1; }
  .web-address {
    position: absolute; top: 770px; left: 780px; width: 368px; text-align: right;
    font-size: 31px; color: var(--ink);
  }
</style>
</head>
<body>
  <div class="backdrop" role="img" aria-label="Soft grey watercolour leaves texture"></div>
  <div class="panel"></div>

  <div class="headline-word headline-unique">UNIQUE</div>
  <div class="headline-word headline-script">You’re</div>

  <p class="tagline">Your Home Should Be Too</p>
  <div class="divider"></div>

  <ul class="finish-list">
    <li class="finish-plaster">Ventian Plaster</li>
    <li class="finish-lime">Lime Wash</li>
    <li class="finish-clay">Roman Clay</li>
    <li class="finish-mineral">Mineral Wash.</li>
  </ul>

  <svg class="project-photos" viewBox="0 0 1200 838" xmlns="http://www.w3.org/2000/svg">
    <defs>
      <linearGradient id="fireplaceTone" x1="0" y1="0" x2="0" y2="1">
        <stop offset="0" stop-color="#d8d6d2"/>
        <stop offset="0.7" stop-color="#b9b6b0"/>
        <stop offset="1" stop-color="#5a5a5a"/>
      </linearGradient>
      <linearGradient id="houseTone" x1="0" y1="0" x2="0" y2="1">
        <stop offset="0" stop-color="#dfe6ea"/>
        <stop offset="0.55" stop-color="#e8e6e2"/>
        <stop offset="1" stop-color="#7d9a5a"/>
      </linearGradient>
      <linearGradient id="brickTone" x1="0" y1="0" x2="1" y2="1">
        <stop offset="0" stop-color="#e4e3e0"/>
        <stop offset="1" stop-color="#b8b7b3"/>
      </linearGradient>
    </defs>
    <circle cx="194" cy="711" r="100" fill="url(#fireplaceTone)" stroke="#1f2a66" stroke-width="6" role="img" aria-label="Limewashed brick fireplace interior"/>
    <circle cx="419" cy="714" r="98" fill="url(#houseTone)" stroke="#1f2a66" stroke-width="6" role="img" aria-label="White limewashed brick house exterior"/>
    <circle cx="311" cy="718" r="52" fill="url(#brickTone)" stroke="#9a9a9c" stroke-width="2" role="img" aria-label="Close-up of limewashed brick"/>
  </svg>

  <div class="brand-lockup">
    <span class="brand-primary">DUNMERE</span>
    <span class="brand-dot"></span>
    <span class="brand-partner">KESTIVA</span>
  </div>
  <p class="web-address">www.dunmerepaints.com</p>
</body>
</html>
```